Bramwell Business Cards

Logo files are included. Full "Bramwell" logo should be included on the back of the business card. The B symbol should be included on the front with the contact information.

Bramwell, LLC is the company name and we do commercial construction and real estate development consulting services. Look for a fairly simple card design utilizing our logo.

```html
<!DOCTYPE html>
<html lang="en">
<head>
<meta charset="utf-8">
<title>Bramwell Business Cards</title>
<link href="https://fonts.googleapis.com/css2?family=Cinzel:wght@600;700&family=Cormorant+Garamond:wght@600&family=Montserrat:wght@600&family=Nunito:wght@500&display=swap" rel="stylesheet">
<style>
  :root {
    --navy: #1b3a50;
    --gold: #e9ad1f;
    --paper: #ffffff;
    --ground: #e4e4e4;
    --ink: #1d1d1d;
  }
  * { margin: 0; padding: 0; box-sizing: border-box; }
  html, body { width: 1200px; height: 1060px; overflow: hidden; }
  body {
    background: var(--ground);
    position: relative;
    font-family: "Nunito", sans-serif;
  }
  .card {
    position: absolute;
    left: 180px;
    width: 840px;
    height: 480px;
    background: var(--paper);
    box-shadow: 0 6px 18px rgba(0,0,0,0.18);
    overflow: hidden;
  }
  .card-back { top: 40px; }
  .card-front { top: 550px; }

  /* back side */
  .edge-mark {
    position: absolute;
    background: var(--gold);
    width: 6px;
    height: 70px;
  }
  .edge-mark-left { left: 0; top: 40px; }
  .edge-mark-right { right: 0; bottom: 60px; }
  .brand-name {
    position: absolute;
    left: 0; right: 0; top: 0; bottom: 0;
    display: flex;
    align-items: center;
    justify-content: center;
    gap: 22px;
    font-family: "Montserrat", sans-serif;
    font-weight: 600;
    font-size: 64px;
    letter-spacing: 4px;
    color: var(--navy);
    text-transform: uppercase;
  }
  .brand-dot {
    width: 30px; height: 30px;
    border-radius: 50%;
    background: var(--gold);
  }

  /* front side */
  .swoosh { position: absolute; left: 0; top: 0; width: 840px; height: 480px; }
  .front-brand {
    position: absolute;
    left: 70px;
    top: 90px;
    display: flex;
    align-items: center;
    gap: 14px;
    font-family: "Montserrat", sans-serif;
    font-weight: 600;
    font-size: 40px;
    letter-spacing: 2px;
    color: var(--navy);
  }
  .front-brand .brand-dot { width: 22px; height: 22px; }
  .person {
    position: absolute;
    right: 50px;
    top: 95px;
    text-align: right;
  }
  .person-name {
    font-family: "Cinzel", serif;
    font-weight: 700;
    font-size: 34px;
    color: var(--navy);
    line-height: 1;
  }
  .person-role {
    display: flex;
    align-items: center;
    justify-content: flex-end;
    gap: 8px;
    margin-top: 6px;
    font-family: "Cormorant Garamond", serif;
    font-weight: 600;
    font-size: 15px;
    color: var(--ink);
  }
  .person-role::before {
    content: "";
    width: 60px;
    height: 1px;
    background: var(--ink);
  }
  .contact-list {
    position: absolute;
    right: 50px;
    top: 220px;
    list-style: none;
    text-align: right;
  }
  .contact-item {
    display: flex;
    align-items: center;
    justify-content: flex-end;
    gap: 12px;
    font-size: 19px;
    color: var(--ink);
    line-height: 1.25;
    margin-bottom: 10px;
  }
  .contact-item.gap-before { margin-top: 10px; }
  .icon {
    flex: none;
    width: 24px; height: 24px;
    border-radius: 50%;
    background: var(--gold);
    display: flex;
    align-items: center;
    justify-content: center;
  }
  .icon svg { width: 13px; height: 13px; fill: var(--navy); }
</style>
</head>
<body>

  <section class="card card-back" aria-label="Card back">
    <span class="edge-mark edge-mark-left"></span>
    <span class="edge-mark edge-mark-right"></span>
    <div class="brand-name"><span class="brand-dot"></span>Bramwell</div>
  </section>

  <section class="card card-front" aria-label="Card front">
    <svg class="swoosh" viewBox="0 0 840 480" aria-hidden="true">
      <path d="M0,288 C260,316 560,420 760,480 L0,480 Z" fill="var(--gold)"/>
      <path d="M0,294 C240,324 470,408 640,480 L0,480 Z" fill="#f6f6f6"/>
      <path d="M0,306 C200,336 360,410 470,480 L0,480 Z" fill="var(--navy)"/>
    </svg>

    <div class="front-brand"><span class="brand-dot"></span>Bramwell</div>

    <div class="person">
      <div class="person-name">Owen Marlow</div>
      <div class="person-role">Founder &amp; Business Head</div>
    </div>

    <ul class="contact-list">
      <li class="contact-item">+1 555 014 2380
        <span class="icon"><svg viewBox="0 0 24 24"><path d="M6.6 10.8a15 15 0 0 0 6.6 6.6l2.2-2.2a1 1 0 0 1 1-.25 11.4 11.4 0 0 0 3.6.57 1 1 0 0 1 1 1V20a1 1 0 0 1-1 1A17 17 0 0 1 3 4a1 1 0 0 1 1-1h3.5a1 1 0 0 1 1 1c0 1.25.2 2.45.57 3.6a1 1 0 0 1-.25 1z"/></svg></span></li>
      <li class="contact-item">+1 555 014 2381
        <span class="icon"><svg viewBox="0 0 24 24"><path d="M7 2h10a2 2 0 0 1 2 2v16a2 2 0 0 1-2 2H7a2 2 0 0 1-2-2V4a2 2 0 0 1 2-2zm0 3v12h10V5zm5 13.2a1 1 0 1 0 0 2 1 1 0 0 0 0-2z"/></svg></span></li>
      <li class="contact-item gap-before">owen.marlow@bramwellco.com
        <span class="icon"><svg viewBox="0 0 24 24"><path d="M3 5h18a1 1 0 0 1 1 1v12a1 1 0 0 1-1 1H3a1 1 0 0 1-1-1V6a1 1 0 0 1 1-1zm1 2.2V17h16V7.2l-8 5.3z"/></svg></span></li>
      <li class="contact-item">www.bramwellco.com
        <span class="icon"><svg viewBox="0 0 24 24"><path d="M12 2a10 10 0 1 0 0 20 10 10 0 0 0 0-20zm6.9 9h-3a15 15 0 0 0-1.3-5.6A8 8 0 0 1 18.9 11zM12 4c.9 1.2 1.8 3.6 1.9 7h-3.8c.1-3.4 1-5.8 1.9-7zM9.4 5.4A15 15 0 0 0 8.1 11h-3a8 8 0 0 1 4.3-5.6zM5.1 13h3a15 15 0 0 0 1.3 5.6A8 8 0 0 1 5.1 13zM12 20c-.9-1.2-1.8-3.6-1.9-7h3.8c-.1 3.4-1 5.8-1.9 7zm2.6-1.4a15 15 0 0 0 1.3-5.6h3a8 8 0 0 1-4.3 5.6z"/></svg></span></li>
      <li class="contact-item gap-before">Your Address, City, State,<br>Country, Zip Code
        <span class="icon"><svg viewBox="0 0 24 24"><path d="M12 2a7 7 0 0 0-7 7c0 5.2 7 13 7 13s7-7.8 7-13a7 7 0 0 0-7-7zm0 9.5A2.5 2.5 0 1 1 12 6.5a2.5 2.5 0 0 1 0 5z"/></svg></span></li>
    </ul>
  </section>

</body>
</html>
```